Business Card Design for Cybersecurity Company - Quorvent Systems

We need a business card design for our new cybersecurity company, Quorvent. We’re going for a clean, hi tech look that feels modern, premium, and trustworthy. We want a design that really stands out and makes people say WOW when we hand it over!

Quorvent delivers reliable IT support and managed services for small and mid sized businesses. We help companies stay secure, efficient, and connected through proactive monitoring, cybersecurity services, cloud management, and remote support.

Target Market(s)

Designers should target small and mid sized businesses that need dependable cybersecurity and IT support.

Industry/Entity Type

Cybersecurity, Managed Service Provider, IT services

Contact Information for Business Card

Contact information

Requirements
Must have
• The card should look clean, modern, and tech focused, with the Quorvent logo, clear contact info, and strong readability. It needs to feel premium and professional while still keeping a simple layout that fits a cybersecurity and IT brand.
Nice to have
• Nice to have elements include subtle touches that give the card a modern, tech feel, along with a layout that works well in different background styles.
Should not have
• The card should avoid clutter, loud graphics, or anything that takes attention away from the logo and contact details.

```html
<!DOCTYPE html>
<html lang="en">
<head>
<meta charset="utf-8">
<title>Quorvent Systems – Business Card</title>
<link href="https://fonts.googleapis.com/css2?family=Lato:wght@400;700&display=swap" rel="stylesheet">
<style>
  :root {
    --backdrop: #242424;
    --gradient-blue: #1e95ff;
    --gradient-purple: #8a2be2;
    --navy-dark: #0c0e2e;
    --navy-mid: #171a45;
    --ink-dark: #15163a;
    --white: #ffffff;
    --accent-blue: #2b8cff;
    --accent-purple: #8b3fe6;
    --text-light: #c9cbd8;
  }
  html, body {
    margin: 0;
    padding: 0;
    width: 1200px;
    height: 939px;
    overflow: hidden;
    background: var(--backdrop);
    font-family: 'Lato', sans-serif;
  }
  .canvas {
    position: relative;
    width: 1200px;
    height: 939px;
  }
  .card {
    position: absolute;
    width: 560px;
    height: 320px;
    border-radius: 18px;
    box-shadow: 0 18px 40px rgba(0,0,0,0.55);
    overflow: hidden;
  }
  .card-front {
    left: 110px;
    top: 90px;
    background: linear-gradient(110deg, var(--gradient-blue) 20%, var(--gradient-purple) 70%);
    display: flex;
    align-items: center;
    justify-content: center;
  }
  .front-wordmark {
    display: flex;
    align-items: center;
    gap: 14px;
    color: var(--ink-dark);
    font-weight: 700;
    font-size: 40px;
    letter-spacing: 0.5px;
  }
  .wordmark-dot {
    width: 26px;
    height: 26px;
    border-radius: 50%;
    background: currentColor;
  }
  .card-back {
    left: 530px;
    top: 530px;
    background: linear-gradient(135deg, var(--navy-mid), var(--navy-dark) 70%);
  }
  .back-decoration {
    position: absolute;
    right: 26px;
    top: 28px;
    width: 250px;
    height: 264px;
    border-radius: 50%;
    background: radial-gradient(closest-side, rgba(43,140,255,0.55), rgba(139,63,230,0.4) 55%, rgba(139,63,230,0) 100%);
  }
  .back-content {
    position: absolute;
    left: 44px;
    top: 58px;
  }
  .back-wordmark {
    display: flex;
    align-items: center;
    gap: 10px;
    color: var(--white);
    font-weight: 700;
    font-size: 30px;
  }
  .back-wordmark .wordmark-dot {
    width: 18px;
    height: 18px;
  }
  .person-name {
    margin-top: 24px;
    color: var(--accent-blue);
    font-weight: 700;
    font-size: 25px;
    letter-spacing: 0.3px;
  }
  .person-title {
    margin-top: 2px;
    color: var(--accent-purple);
    font-size: 16px;
  }
  .contact-list {
    list-style: none;
    margin: 16px 0 0;
    padding: 0;
  }
  .contact-list li {
    display: flex;
    align-items: center;
    gap: 10px;
    color: var(--text-light);
    font-size: 15px;
    line-height: 24px;
  }
  .contact-list svg {
    width: 13px;
    height: 13px;
    fill: var(--accent-blue);
    flex: none;
  }
</style>
</head>
<body>
<main class="canvas">
  <section class="card card-front" aria-label="Card front">
    <div class="front-wordmark">
      <span class="wordmark-dot"></span>
      <span>Quorvent Systems</span>
    </div>
  </section>

  <section class="card card-back" aria-label="Card back">
    <div class="back-decoration" role="img" aria-label="Large glowing brand graphic in blue and purple"></div>
    <div class="back-content">
      <div class="back-wordmark">
        <span class="wordmark-dot"></span>
        <span>Quorvent Systems</span>
      </div>
      <div class="person-name">DANA MERROW</div>
      <div class="person-title">Owner / CEO</div>
      <ul class="contact-list">
        <li>
          <svg viewBox="0 0 16 16"><path d="M3 1l3 3-1.5 2a9 9 0 0 0 5.5 5.5L12 10l3 3-2 2C7 15 1 9 1 3z"/></svg>
          (855) 400-QRVT
        </li>
        <li>
          <svg viewBox="0 0 16 16"><path d="M4 0h8a1 1 0 0 1 1 1v14a1 1 0 0 1-1 1H4a1 1 0 0 1-1-1V1a1 1 0 0 1 1-1zm1 2v10h6V2zm3 11a1 1 0 1 0 0 2 1 1 0 0 0 0-2z"/></svg>
          (813) 555-0187
        </li>
        <li>
          <svg viewBox="0 0 16 16"><path d="M0 3h16v1L8 9 0 4zm0 3l8 5 8-5v7H0z"/></svg>
          dana@quorvent.com
        </li>
        <li>
          <svg viewBox="0 0 16 16"><path d="M8 0a8 8 0 1 0 0 16A8 8 0 0 0 8 0zm0 1.5c.9 1 1.6 2.8 1.8 5.5H6.2C6.4 4.3 7.1 2.5 8 1.5zM1.6 9h3.1c.1 2 .6 3.8 1.3 5A6.5 6.5 0 0 1 1.6 9zm0-2A6.5 6.5 0 0 1 6 2c-.7 1.2-1.2 3-1.3 5zm6.4 7.5c-.9-1-1.6-2.8-1.8-5.5h3.6c-.2 2.7-.9 4.5-1.8 5.5zM10 14c.7-1.2 1.2-3 1.3-5h3.1a6.5 6.5 0 0 1-4.4 5zm1.3-7c-.1-2-.6-3.8-1.3-5a6.5 6.5 0 0 1 4.4 5z"/></svg>
          quorvent.com
        </li>
      </ul>
    </div>
  </section>
</main>
</body>
</html>
```